Smart Coffee Shop Needs a Poster Design

New smart coffee shop called Brewlo using touch screens as table tops. all information in attached file. the café is now open in a busy mall in Abu Dhabi.
We need creative design for 2 posters on two sides of a column. This is to attract the attention of people from a distance. We need it to be colorful and preferably in two languages: English and Arabic.
The dimensions are: 275 (H) x 75 (W) cm & 275 (H) x 87 (W) cm.
Catch phrase could be: The Smartest and Coolest Café on Earth. or something similar. Attached also is the hoarding poster.
Updates
Project Deadline Extended
Reason: Received 8 designs only. Still looking for more creative ideas. If we select your design, we will be providing more jobs (website, facebook, brochures, flyers, more posters etc..).
Industry/Entity Type
Coffee Shop
Look and feel
Each slider illustrates characteristics of the customer's brand and the style your logo design should communicate.

```html
<!DOCTYPE html>
<html lang="en">
<head>
<meta charset="utf-8">
<title>Brewlo column banners</title>
<link rel="stylesheet" href="https://fonts.googleapis.com/css2?family=Fredoka:wght@600&family=Open+Sans:wght@400&display=swap">
<style>
  :root {
    --stage-top: #f3f4f8;
    --stage-bottom: #dcdee6;
    --space-magenta: #6a2a63;
    --space-violet: #3a2a6e;
    --space-navy: #1c1f4f;
    --space-deep: #141838;
    --earth-glow: #6fb6ea;
    --earth-blue: #1f5f9c;
    --ink-white: #ffffff;
    --label-grey: #555a63;
    --panel-fill: rgba(150, 150, 220, 0.22);
    --panel-edge: rgba(255, 255, 255, 0.35);
  }
  * { box-sizing: border-box; margin: 0; padding: 0; }
  html, body { width: 1200px; height: 1200px; overflow: hidden; }
  body {
    position: relative;
    background: linear-gradient(180deg, var(--stage-top), var(--stage-bottom));
    font-family: "Fredoka", "Trebuchet MS", sans-serif;
    font-weight: 600;
    color: var(--ink-white);
  }
  .banner {
    position: absolute;
    top: 58px;
    height: 1022px;
    overflow: hidden;
    box-shadow: 6px 6px 14px rgba(0, 0, 0, 0.35);
  }
  .banner--narrow { left: 268px; width: 278px; }
  .banner--wide { left: 608px; width: 322px; }
  .banner__backdrop {
    position: absolute;
    inset: 0;
    background:
      radial-gradient(140% 28% at 50% 100%, var(--earth-glow) 0%, var(--earth-blue) 35%, transparent 70%),
      linear-gradient(180deg, var(--space-magenta) 0%, var(--space-violet) 18%, var(--space-navy) 45%, var(--space-deep) 65%, var(--earth-blue) 100%);
  }
  .brand {
    position: absolute;
    left: 0; right: 0;
    top: 168px;
    text-align: center;
    font-size: 52px;
    line-height: 1;
  }
  .headline-panel {
    position: absolute;
    left: 20px; right: 20px;
    top: 280px;
    height: 328px;
    background: var(--panel-fill);
    border: 2px solid var(--panel-edge);
    border-radius: 8px;
    display: flex;
    align-items: center;
    justify-content: center;
  }
  .headline-panel__text {
    text-align: center;
    font-size: 34px;
    line-height: 47px;
    text-transform: uppercase;
    white-space: nowrap;
  }
  .invite {
    position: absolute;
    left: 0; right: 0;
    top: 628px;
    text-align: center;
    text-transform: uppercase;
    font-size: 21px;
    line-height: 30px;
    white-space: nowrap;
  }
  .invite__key { font-size: 26px; }
  .slanted-block {
    position: absolute;
    left: 36px;
    top: 300px;
    width: 250px;
    transform: rotate(-12deg);
    transform-origin: center center;
    text-transform: uppercase;
    text-align: right;
    white-space: nowrap;
  }
  .slanted-block__line { display: block; line-height: 0.98; }
  .slanted-block__the { font-size: 40px; text-align: left; padding-left: 30px; }
  .slanted-block__smartest { font-size: 45px; }
  .slanted-block__coolest { font-size: 32px; }
  .slanted-block__cafe { font-size: 86px; line-height: 1; }
  .slanted-block__earth { font-size: 54px; text-align: left; }
  .slanted-block__on { font-size: 28px; }
  .slanted-block__rule {
    display: block;
    width: 232px;
    height: 3px;
    background: var(--ink-white);
    margin: 18px 0 12px;
  }
  .slanted-block__invite {
    font-size: 14px;
    letter-spacing: 2.5px;
    text-align: left;
    line-height: 20px;
  }
  .slanted-block__invite-key { font-size: 15px; letter-spacing: 0.5px; }
  .size-label {
    position: absolute;
    top: 1093px;
    font-family: "Open Sans", Arial, sans-serif;
    font-weight: 400;
    font-size: 26px;
    color: var(--label-grey);
    text-align: center;
  }
  .size-label--narrow { left: 237px; width: 340px; }
  .size-label--wide { left: 598px; width: 340px; }
</style>
</head>
<body>
  <section class="banner banner--narrow">
    <div class="banner__backdrop" role="img" aria-label="Starry purple and blue space scene with a geometric line network, glowing Earth at the bottom"></div>
    <div class="brand">Brewlo</div>
    <div class="headline-panel">
      <p class="headline-panel__text">The<br>smartest<br>and<br>coolest<br>café on<br>earth</p>
    </div>
    <p class="invite">Come in and try<br>our interactive<br><span class="invite__key">smart tables</span></p>
  </section>

  <section class="banner banner--wide">
    <div class="banner__backdrop" role="img" aria-label="Starry purple and blue space scene with a geometric line network, glowing Earth at the bottom"></div>
    <div class="brand">Brewlo</div>
    <div class="slanted-block">
      <span class="slanted-block__line slanted-block__the">The</span>
      <span class="slanted-block__line slanted-block__smartest">Smartest</span>
      <span class="slanted-block__line slanted-block__coolest">and coolest</span>
      <span class="slanted-block__line slanted-block__cafe">Café</span>
      <span class="slanted-block__line slanted-block__earth"><span class="slanted-block__on">on </span>Earth</span>
      <span class="slanted-block__rule"></span>
      <span class="slanted-block__line slanted-block__invite">Come in and try our</span>
      <span class="slanted-block__line slanted-block__invite slanted-block__invite-key">Interactive smart tables</span>
    </div>
  </section>

  <p class="size-label size-label--narrow">75 cm x 275 cm</p>
  <p class="size-label size-label--wide">87 cm x 275 cm</p>
</body>
</html>
```